7Brink Plumbing flyer

I want to incorporate our logo design into a new flyer promoting the business and advertising products that we install.
We install hot water systems, Air-conditioning systems and central heating systems. Along with other aspects of plumbing such as gasfitting, roofing, sanitary and drainage
I would like the background to be the same as our business cards with the water effect and colours.

Requirements
Must have
• Logo
24/7 Emergency call out
Aspects of plumbing we do
- Hot water systems
- Central Heating
- Solar hot water systems/ heat pump systems
- Gasfitting
- Drainage
- Roofing
- Air-Conditioning
Nice to have
• Pictures of hot water systems and air-conditioning system
$30 off voucher when producing this flyer (limit 1 per house hold)

```html
<!DOCTYPE html>
<html lang="en">
<head>
<meta charset="utf-8">
<title>7Brink Plumbing Flyer</title>
<link href="https://fonts.googleapis.com/css2?family=Exo+2:wght@700;800;900&display=swap" rel="stylesheet">
<style>
  :root{
    --stage:#1a8fd6;
    --slate:#45484d;
    --slate-dark:#3a3d42;
    --blue:#1d8fdc;
    --blue-bright:#27a6ef;
    --ink:#3b3e45;
    --white:#ffffff;
  }
  *{margin:0;padding:0;box-sizing:border-box}
  html,body{width:1019px;height:1200px;overflow:hidden;background:var(--stage)}
  body{font-family:"Exo 2",sans-serif;position:relative}
  .flyer{position:absolute;left:86px;top:0;width:847px;height:1200px;background:var(--slate);overflow:hidden}
  .flyer-shapes{position:absolute;inset:0}
  .txt{position:absolute;text-transform:uppercase;font-weight:900;line-height:1}
  .brand{left:586px;top:60px;color:var(--blue-bright)}
  .brand-name{display:block;font-size:36px;font-weight:800;line-height:.95;letter-spacing:.5px}
  .brand-sub{display:block;font-size:14px;font-weight:700;color:#d9dde2;margin-top:2px}
  .brand-phone{display:block;font-size:23px;font-weight:700;margin-top:1px;letter-spacing:1px}
  .headline{left:430px;width:420px;top:214px;text-align:center}
  .headline-kicker{display:block;font-size:25px;color:#bfe3fb;letter-spacing:.5px}
  .headline-main{display:block;font-size:52px;line-height:.95;margin-top:4px;
    background:linear-gradient(180deg,#ffffff 0%,#d7efff 40%,#2a9fe8 100%);
    -webkit-background-clip:text;background-clip:text;color:transparent}
  .badge{left:578px;top:398px;width:170px;text-align:center;color:var(--white)}
  .badge-big{display:block;font-size:50px;letter-spacing:-1px}
  .badge-mid{display:block;font-size:19px;margin-top:2px}
  .badge-small{display:block;font-size:17px;margin-top:6px}
  .intro{left:84px;width:706px;top:562px;text-align:center;color:var(--ink);font-size:21.5px;line-height:30.5px;font-weight:800}
  .we-do{left:34px;top:1048px;transform-origin:left top;transform:rotate(-90deg) translate(-120px,0);
    color:var(--white);font-size:50px;letter-spacing:1px;width:240px;text-align:center;top:1166px;left:30px;transform:rotate(-90deg)}
  .services{position:absolute;left:90px;top:929px;width:321px;list-style:none}
  .services li{height:30px;margin-bottom:4.3px;border-radius:15px;background:var(--blue);
    color:var(--white);font-weight:800;font-size:14px;text-transform:uppercase;line-height:30px;padding-left:22px}
  .contact{left:455px;width:390px;top:932px;text-align:center}
  .call-now{display:block;font-size:54px;background:linear-gradient(180deg,#ffffff 0%,#cfeaff 45%,#1f97e6 100%);
    -webkit-background-clip:text;background-clip:text;color:transparent}
  .call-phone{display:block;font-size:34px;color:var(--blue-bright);margin-top:8px}
  .call-mail{display:block;font-size:21px;color:#7cc9f7;text-transform:none;font-weight:800;margin-top:20px}
  .social-box{display:block;width:28px;height:28px;border:2.5px solid var(--blue-bright);border-radius:4px;margin:14px auto 0}
  .social-handle{display:block;font-size:23px;color:#7cc9f7;text-transform:none;font-weight:800;margin-top:8px}
</style>
</head>
<body>
<main class="flyer">
  <svg class="flyer-shapes" width="847" height="1200" viewBox="0 0 847 1200">
    <defs>
      <linearGradient id="heroTone" x1="0" y1="0" x2="1" y2="0">
        <stop offset="0" stop-color="#6f7a6a"/>
        <stop offset=".25" stop-color="#8c9096"/>
        <stop offset=".6" stop-color="#6c7076"/>
        <stop offset="1" stop-color="#45484d"/>
      </linearGradient>
      <linearGradient id="productTone" x1="0" y1="0" x2="0" y2="1">
        <stop offset="0" stop-color="#f4f6f8"/>
        <stop offset="1" stop-color="#c9ced4"/>
      </linearGradient>
      <radialGradient id="badgeTone" cx=".5" cy=".4" r=".6">
        <stop offset="0" stop-color="#2aa6ef"/>
        <stop offset="1" stop-color="#1580cc"/>
      </radialGradient>
    </defs>
    <rect class="hero-photo" x="0" y="0" width="560" height="520" fill="url(#heroTone)" role="img" aria-label="Photo of a wall-mounted continuous-flow hot water unit with copper pipes beside a green shrub"/>
    <path class="mid-band" d="M0 365 C60 470 140 525 260 520 C420 512 560 460 700 450 C770 446 820 452 847 456 L847 800 C700 760 560 760 400 800 C250 840 120 820 0 752 Z" fill="#ffffff"/>
    <path class="wave-top" d="M0 365 C60 470 140 525 260 520 C420 512 560 460 700 450 C770 446 820 452 847 456" fill="none" stroke="var(--blue)" stroke-width="14"/>
    <path class="wave-bottom" d="M0 752 C120 820 250 840 400 800 C560 760 700 760 847 800" fill="none" stroke="#ffffff" stroke-width="6"/>
    <circle class="logo-dot" cx="522" cy="98" r="48" fill="none" stroke="var(--blue)" stroke-width="8"/>
    <circle cx="663" cy="451" r="96" fill="#ffffff"/>
    <circle cx="663" cy="451" r="91" fill="url(#badgeTone)" stroke="var(--blue)" stroke-width="3"/>
    <circle cx="663" cy="451" r="84" fill="none" stroke="#ffffff" stroke-width="3"/>
    <circle class="product-photo" cx="124" cy="789" r="94" fill="url(#productTone)" stroke="var(--blue)" stroke-width="6" role="img" aria-label="Hot water storage tank, continuous-flow unit and solar collector panel"/>
    <circle class="product-photo" cx="323" cy="811" r="86" fill="url(#productTone)" stroke="var(--blue)" stroke-width="6" role="img" aria-label="Split-system air-conditioner outdoor unit"/>
    <circle class="product-photo" cx="508" cy="802" r="69" fill="url(#productTone)" stroke="var(--blue)" stroke-width="6" role="img" aria-label="Ceiling cassette heating and cooling unit"/>
    <line x1="447" y1="931" x2="447" y2="1170" stroke="var(--blue)" stroke-width="3"/>
  </svg>

  <div class="txt brand">
    <span class="brand-name">7Brink<br>Plumbing</span>
    <span class="brand-sub">&amp; Air-Conditioning</span>
    <span class="brand-phone">0400 555 017</span>
  </div>

  <h1 class="txt headline">
    <span class="headline-kicker">We Install</span>
    <span class="headline-main">Hot Water<br>Systems</span>
  </h1>

  <div class="txt badge">
    <span class="badge-big">24/7</span>
    <span class="badge-mid">Emergency</span>
    <span class="badge-small">Call Out</span>
  </div>

  <p class="txt intro">We install hot water systems, air-conditioning systems and central heating systems. Along with other aspects of plumbing such as gasfitting, roofing, sanitary and drainage</p>

  <div class="txt we-do">We Do</div>
  <ul class="services">
    <li>Hot Water Systems</li>
    <li>Central Heating</li>
    <li>Solar Hot Water Systems</li>
    <li>Heat Pump Systems</li>
    <li>Gasfitting</li>
    <li>Drainage &nbsp;&nbsp;&nbsp;•&nbsp;&nbsp;&nbsp; Roofing</li>
    <li>Air-Conditioning</li>
  </ul>

  <div class="txt contact">
    <span class="call-now">Call Now</span>
    <span class="call-phone">+61 400 555 017</span>
    <span class="call-mail">sam@7brinkplumbing.com</span>
    <span class="social-box"></span>
    <span class="social-handle">/7brinkplumbing/</span>
  </div>
</main>
</body>
</html>
```